Custom Made Digital Jukebox sales and rental website

I need a design for a Custom Made Digital Jukebox sales and rental services website. Domain name is quelitrune.com. Exisiting customer shall have a section to register, login/logout, my account, support. All other visitor shall have at least the following options or menu avaialble: Home, FAQ, Services, Products, and Contact us. I have attached a high level requirements pdf file. Please don't be limited by high level requirements file attached, your idea may be better than what I specified. My products are designed base on customer requirements. Common parts are: Bill and Coin Acceptors, Touchscreen or keypad. All of them are wall mount.

Target Market(s)

Custom made digital Jukebox for Home and Commercial use

Industry/Entity Type

Digital

Number of Pages Required

1 page

Requirements
Must have
• PSD required.
Nice to have
• HTML code and CSS Stylesheet
• Logo for QueliTrune
• Inner Pages
Should not have
• Copyright material from related websites, previously developed or any other.

```html
<!DOCTYPE html>
<html lang="en">
<head>
<meta charset="utf-8">
<title>QueliTrune – Digital Jukebox Sales &amp; Rental</title>
<link rel="stylesheet" href="https://fonts.googleapis.com/css2?family=Roboto:wght@300;400;500;700&family=Roboto+Condensed:wght@400;700&display=swap">
<style>
:root{
  --orange:#f39200;
  --orange-dark:#c96f00;
  --blue:#1e8fd6;
  --teal:#2aa6c9;
  --teal-dark:#167f9e;
  --ink:#1a1a1a;
  --charcoal:#2b2b2b;
  --nav:#3a3a3a;
  --grey:#8a8a8a;
  --white:#ffffff;
  --footer:#1e1f21;
}
*{box-sizing:border-box;margin:0;padding:0}
html,body{width:833px;height:1200px;overflow:hidden}
body{font-family:"Roboto",Arial,sans-serif;background:var(--white);color:var(--ink);position:relative}
.page{width:833px;height:1200px;position:relative}

/* header */
.site-header{height:67px;display:flex;align-items:center;justify-content:space-between;padding:0 60px;border-bottom:1px solid #e2e2e2}
.brand{display:flex;align-items:center;gap:8px;font-weight:500;font-size:20px;letter-spacing:1px;color:var(--teal)}
.brand-dot{width:12px;height:12px;background:var(--orange)}
.account-links{display:flex;align-items:center;gap:10px;font-size:10px;color:#444}
.account-links span.sep{color:#bbb}
.cart{margin-left:18px;display:flex;align-items:center;gap:6px;font-size:10px;color:#555;border:1px solid #ddd;padding:4px 8px}
.cart svg{width:12px;height:12px}

/* nav */
.main-nav{height:38px;background:var(--nav);border-bottom:3px solid var(--orange);display:flex;align-items:center;padding:0 60px}
.main-nav a{color:#eee;text-decoration:none;font-size:11px;font-weight:500;padding:0 22px;height:35px;display:flex;align-items:center;letter-spacing:.5px}
.main-nav a.active{background:#222}
.search{margin-left:auto;display:flex;height:22px}
.search span{width:120px;background:#fff;font-size:10px;color:#888;padding:5px 7px}
.search b{width:22px;background:#222;display:flex;align-items:center;justify-content:center}
.search svg{width:11px;height:11px}

/* hero */
.hero{position:relative;height:370px;overflow:hidden}
.hero-photo{position:absolute;inset:0;background:radial-gradient(ellipse at 45% 20%,#f6b35a 0%,#b9651d 22%,#3b2210 50%,#0c0907 80%)}
.hero-copy{position:absolute;left:125px;top:105px;color:#fff}
.hero-copy h1{font-family:"Roboto Condensed",Arial,sans-serif;font-size:38px;font-weight:400;letter-spacing:1px}
.hero-copy h2{font-family:"Roboto Condensed",Arial,sans-serif;font-size:40px;font-weight:400;margin-top:4px}
.hero-copy h2 em{font-style:normal;color:var(--orange)}
.btn{display:inline-block;color:#fff;font-size:12px;font-weight:500;letter-spacing:.5px;text-decoration:none}
.btn-blue{background:var(--blue);padding:13px 26px;margin-top:18px}
.hero-product{position:absolute;left:485px;top:10px;width:205px;height:352px;background:linear-gradient(160deg,#4a4a4a,#111 60%,#2f2f2f);border-radius:3px;transform:skewY(3deg)}
.slide-arrow{position:absolute;top:190px;width:22px;height:30px;background:rgba(0,0,0,.5);display:flex;align-items:center;justify-content:center}
.slide-arrow svg{width:9px;height:12px}
.slide-arrow.prev{left:44px}.slide-arrow.next{right:44px}

/* promos */
.promos{display:flex;height:188px;margin-top:8px}
.promo{flex:1;position:relative;overflow:hidden;color:#fff;padding:38px 0 0 40px}
.promo-sales{background:linear-gradient(90deg,#6a3a10,#2a1a10)}
.promo-rental{background:linear-gradient(90deg,#0f3246,#153f58);border-top:4px solid var(--teal)}
.promo .eyebrow{font-family:"Roboto Condensed",Arial,sans-serif;font-size:18px;color:var(--orange);font-weight:700}
.promo-rental .eyebrow{color:var(--teal)}
.promo h3{font-size:15px;font-weight:500;margin-top:8px}
.btn-orange{background:var(--orange);padding:9px 18px;margin-top:18px;font-size:10px}
.btn-teal{background:var(--blue);padding:9px 22px;margin-top:18px;font-size:10px}
.promo-image{position:absolute;top:30px;width:78px;height:130px;border-radius:4px}
.promo-sales .promo-image{left:258px;background:linear-gradient(160deg,#555,#111)}
.promo-rental .promo-image{left:255px;background:radial-gradient(ellipse at 50% 25%,#f0b040,#a0401a 60%,#4a1a0a)}

/* products */
.products{position:relative;height:290px;margin-top:8px;background:radial-gradient(ellipse at 50% 0%,#5a5a5a,#262626 55%,#151515);padding:22px 60px 0}
.products-head{display:flex;justify-content:space-between;align-items:center;color:#fff}
.products-head h2{font-family:"Roboto Condensed",Arial,sans-serif;font-size:20px;font-weight:400}
.carousel-nav{display:flex;gap:6px}
.carousel-nav svg{width:10px;height:16px}
.product-grid{display:flex;gap:8px;margin-top:16px}
.product-card{flex:1;height:165px;background:var(--teal);position:relative;text-align:center;color:#fff;padding-top:14px}
.product-card .thumb{width:48px;height:92px;margin:0 auto;border-radius:3px}
.product-card:nth-child(1) .thumb{background:linear-gradient(160deg,#555,#0d0d0d)}
.product-card:nth-child(2) .thumb{background:linear-gradient(160deg,#6b6b6b,#1c1c1c)}
.product-card:nth-child(3) .thumb{background:radial-gradient(ellipse at 50% 30%,#f2b447,#9b3b18 65%)}
.product-card:nth-child(4) .thumb{background:linear-gradient(160deg,#444,#050505)}
.product-card .name{font-size:10px;margin-top:12px}
.product-card .price{font-size:10px;margin-top:8px}
.add-cart{position:absolute;right:0;bottom:0;width:22px;height:22px;background:var(--orange);display:flex;align-items:center;justify-content:center}
.add-cart svg{width:12px;height:12px}

/* footer */
.site-footer{height:195px;background:var(--footer);color:#bbb;display:flex;gap:34px;padding:22px 60px 0;font-size:9.5px;line-height:1.6}
.site-footer h4{color:#fff;font-size:13px;font-weight:400;margin-bottom:8px;font-family:"Roboto Condensed",Arial,sans-serif;letter-spacing:.5px}
.footer-contact{width:180px}
.footer-account{width:100px}
.footer-account ul{list-style:none}
.footer-news{width:175px}
.news-field{display:flex;margin-top:4px}
.news-field span{flex:1;height:18px;background:#fff}
.news-field b{width:18px;height:18px;background:#333;border:1px solid #555}
.pay-label{margin-top:10px}
.pay-cards{display:flex;gap:4px;margin-top:4px}
.pay-cards i{width:22px;height:14px;background:#d8d8d8;display:block}
.social-widget{width:120px;height:120px;background:#fff;color:#444;padding:6px;font-size:8px;line-height:1.4}
.social-widget .w-name{color:var(--teal);font-weight:500;font-size:9px}
.social-widget .w-body{height:72px;background:linear-gradient(135deg,#d5d9df,#eef0f3);margin-top:5px}

/* copyright */
.copy-bar{position:absolute;left:0;right:0;bottom:0;height:57px;background:var(--teal);display:flex;align-items:center;justify-content:space-between;padding:0 60px;color:#e8f6fb;font-size:9px}
.social{display:flex;gap:6px}
.social i{display:block;width:16px;height:16px;background:var(--teal-dark)}
</style>
</head>
<body>
<div class="page">

  <header class="site-header">
    <div class="brand"><span class="brand-dot"></span>QUELITRUNE</div>
    <div class="account-links">
      <span>LOGIN</span><span class="sep">|</span><span>MY ACCOUNT</span><span class="sep">|</span><span>SUPPORT</span>
      <div class="cart">
        <svg viewBox="0 0 12 12"><path d="M1 2h2l1.5 6h5L11 4H4" fill="none" stroke="#f39200" stroke-width="1.3"/><circle cx="5" cy="10.5" r="1" fill="#f39200"/><circle cx="9" cy="10.5" r="1" fill="#f39200"/></svg>
        0 item(s) - $0.00
      </div>
    </div>
  </header>

  <nav class="main-nav">
    <a class="active">HOME</a><a>FAQ</a><a>SERVICES</a><a>PRODUCTS</a><a>CONTACT US</a>
    <div class="search"><span>Search</span><b><svg viewBox="0 0 11 11"><circle cx="4.5" cy="4.5" r="3.3" fill="none" stroke="#fff" stroke-width="1.4"/><path d="M7 7l3 3" stroke="#fff" stroke-width="1.4"/></svg></b></div>
  </nav>

  <section class="hero">
    <div class="hero-photo" role="img" aria-label="Concert crowd with hands raised under warm stage lights"></div>
    <div class="hero-copy">
      <h1>DIGITAL JUKEBOX</h1>
      <h2><em>20%</em> SAVE</h2>
      <a class="btn btn-blue">BUY NOW</a>
    </div>
    <div class="hero-product" role="img" aria-label="Wall-mounted digital jukebox with touchscreen"></div>
    <div class="slide-arrow prev"><svg viewBox="0 0 9 12"><path d="M7 1L2 6l5 5" fill="none" stroke="#fff" stroke-width="1.6"/></svg></div>
    <div class="slide-arrow next"><svg viewBox="0 0 9 12"><path d="M2 1l5 5-5 5" fill="none" stroke="#fff" stroke-width="1.6"/></svg></div>
  </section>

  <section class="promos">
    <div class="promo promo-sales">
      <div class="eyebrow">SALES</div>
      <h3>DIGITAL JUKEBOX</h3>
      <a class="btn btn-orange">BUY NOW</a>
      <div class="promo-image" role="img" aria-label="Digital jukebox for sale"></div>
    </div>
    <div class="promo promo-rental">
      <div class="eyebrow">RENTAL SERVICES</div>
      <h3>DIGITAL JUKEBOX</h3>
      <a class="btn btn-teal">RENTAL</a>
      <div class="promo-image" role="img" aria-label="Classic style jukebox available for rental"></div>
    </div>
  </section>

  <section class="products">
    <div class="products-head">
      <h2>PRODUCTS</h2>
      <div class="carousel-nav">
        <svg viewBox="0 0 10 16"><path d="M8 1L2 8l6 7" fill="none" stroke="#aaa" stroke-width="1.6"/></svg>
        <svg viewBox="0 0 10 16"><path d="M2 1l6 7-6 7" fill="none" stroke="#aaa" stroke-width="1.6"/></svg>
      </div>
    </div>
    <div class="product-grid">
      <article class="product-card"><div class="thumb" role="img" aria-label="Jukebox product"></div><div class="name">PRODUCT NAME</div><div class="price">$00.00</div><span class="add-cart"><svg viewBox="0 0 12 12"><path d="M1 2h2l1.5 6h5L11 4H4" fill="none" stroke="#fff" stroke-width="1.3"/></svg></span></article>
      <article class="product-card"><div class="thumb" role="img" aria-label="Jukebox product"></div><div class="name">PRODUCT NAME</div><div class="price">$00.00</div><span class="add-cart"><svg viewBox="0 0 12 12"><path d="M1 2h2l1.5 6h5L11 4H4" fill="none" stroke="#fff" stroke-width="1.3"/></svg></span></article>
      <article class="product-card"><div class="thumb" role="img" aria-label="Jukebox product"></div><div class="name">PRODUCT NAME</div><div class="price">$00.00</div><span class="add-cart"><svg viewBox="0 0 12 12"><path d="M1 2h2l1.5 6h5L11 4H4" fill="none" stroke="#fff" stroke-width="1.3"/></svg></span></article>
      <article class="product-card"><div class="thumb" role="img" aria-label="Jukebox product"></div><div class="name">PRODUCT NAME</div><div class="price">$00.00</div><span class="add-cart"><svg viewBox="0 0 12 12"><path d="M1 2h2l1.5 6h5L11 4H4" fill="none" stroke="#fff" stroke-width="1.3"/></svg></span></article>
    </div>
  </section>

  <footer class="site-footer">
    <div class="footer-contact">
      <h4>CONTACT US</h4>
      <p>Lorem Ipsum has been the standard dummy text ever since when an unknown printer</p>
      <p>Tel: +0100 555 0199</p>
      <p>Email: hello@quelitrune.com</p>
    </div>
    <div class="footer-account">
      <h4>MY ACCOUNT</h4>
      <ul><li>Your Account</li><li>My orders</li><li>My credit slips</li><li>My addresses</li><li>Login</li></ul>
    </div>
    <div class="footer-news">
      <h4>NEWSLETTER</h4>
      <p>Sign Up For Our Newsletter</p>
      <div class="news-field"><span></span><b></b></div>
      <p class="pay-label">Payment</p>
      <div class="pay-cards"><i></i><i></i><i></i><i></i><i></i></div>
    </div>
    <div class="social-widget">
      <div class="w-name">QUELITRUNE</div>
      <div>1,234 people follow us</div>
      <div class="w-body" role="img" aria-label="Social page preview"></div>
    </div>
  </footer>

  <div class="copy-bar">
    <span>Copyright © 2015. All rights reserved</span>
    <div class="social"><i></i><i></i><i></i><i></i></div>
  </div>

</div>
</body>
</html>
```